Daily special re designs for Hospitality Business / Brewery

Need our daily special social images redone - details as follow and examples attached

I am looking to get an Instagram Square, Facebook Event Cover done for the following promotions:

Meat Free Mondays
Tuesday Scnhitty & Beer for $10.48
Wednesdays - $1 Chicken Wings
Thursdays $15 Pizzas
Friday Burger & Beer for $10.48 12-2pm.
Saturday Half Priced Burgers 12-2pm
Sunday $15 Cocktail Jugs & Live Music

Also need a A3 poster of all the deals combined for in venue use and also a newspaper ad 260mm w x 92mm h

```html
<!DOCTYPE html>
<html lang="en">
<head>
<meta charset="utf-8">
<title>Meat-Free Mondays – Red Ridge Brewing Co</title>
<link href="https://fonts.googleapis.com/css2?family=Montserrat:wght@800&family=Playball&family=Great+Vibes&display=swap" rel="stylesheet">
<style>
  :root {
    --paper: #ffffff;
    --ink: #0b0b0b;
    --leaf-green: #13a14b;
    --leaf-dark: #2f6b1f;
    --leaf-mid: #4f9a2e;
    --leaf-light: #8cc152;
  }
  html, body {
    margin: 0;
    padding: 0;
    overflow: hidden;
    background: var(--paper);
  }
  .poster {
    position: relative;
    width: 1200px;
    height: 1200px;
    background: var(--paper);
    overflow: hidden;
  }
  .produce-band {
    position: absolute;
    inset: 0;
    width: 1200px;
    height: 1200px;
  }
  .brand {
    position: absolute;
    left: 82px;
    top: 58px;
    width: 300px;
    display: flex;
    align-items: center;
    gap: 16px;
    font-family: "Montserrat", sans-serif;
    font-weight: 800;
    color: var(--ink);
  }
  .brand-dot {
    flex: none;
    width: 56px;
    height: 56px;
    border-radius: 50%;
    background: var(--ink);
  }
  .brand-name {
    font-size: 27px;
    line-height: 1.12;
    letter-spacing: 1px;
    text-transform: uppercase;
  }
  .headline {
    position: absolute;
    right: 78px;
    top: 640px;
    margin: 0;
    text-align: right;
    font-weight: normal;
  }
  .headline-script {
    display: block;
    font-family: "Playball", cursive;
    font-size: 118px;
    line-height: 1;
    color: var(--leaf-green);
  }
  .headline-day {
    display: block;
    margin-top: -4px;
    font-family: "Montserrat", sans-serif;
    font-weight: 800;
    font-size: 99px;
    line-height: 1;
    letter-spacing: 2px;
    color: var(--ink);
  }
  .tagline {
    position: absolute;
    right: 70px;
    top: 975px;
    margin: 0;
    font-family: "Great Vibes", cursive;
    font-size: 44px;
    color: var(--ink);
    white-space: nowrap;
  }
</style>
</head>
<body>
  <main class="poster">
    <svg class="produce-band" viewBox="0 0 1200 1200" role="img" aria-label="Photo of a salad tossed from a glass bowl: spinach leaves, kiwi, mandarin segments, red capsicum, cauliflower and cherry tomatoes sweeping from bottom left to top right">
      <defs>
        <linearGradient id="produce-gradient" x1="0" y1="1" x2="1" y2="0">
          <stop offset="0" stop-color="var(--leaf-dark)"/>
          <stop offset="0.45" stop-color="var(--leaf-mid)"/>
          <stop offset="1" stop-color="var(--leaf-light)"/>
        </linearGradient>
      </defs>
      <path fill="url(#produce-gradient)" d="M0 700 C60 560 150 380 260 320 C380 250 470 200 560 160 C690 100 800 40 880 0 L1200 0 L1200 330 C1120 360 1060 420 1020 480 C960 450 900 420 860 400 C760 380 620 420 540 520 C480 600 470 720 450 830 C440 960 450 1080 440 1200 L0 1200 Z"/>
    </svg>

    <div class="brand">
      <span class="brand-dot"></span>
      <span class="brand-name">Red Ridge<br>Brewing Co</span>
    </div>

    <h1 class="headline">
      <span class="headline-script">Meat-Free</span>
      <span class="headline-day">MONDAYS</span>
    </h1>

    <p class="tagline">Great Vegetarian and Vegan Specials</p>
  </main>
</body>
</html>
```